Tallowmere Contracting Business Cards

Front of card:

Full Logo
Name
Address
Office Phone
Cell Phone
Email
Website

Back:
Logo Mark in background
List and markets and services performed

```html
<!DOCTYPE html>
<html lang="en">
<head>
<meta charset="utf-8">
<title>Tallowmere Contracting Business Cards</title>
<link href="https://fonts.googleapis.com/css2?family=Lato:wght@400;700;900&display=swap" rel="stylesheet">
<style>
  :root {
    --backdrop: #2c3032;
    --brand-red: #d92123;
    --ink: #2a2a2a;
    --steel: #6d6e70;
    --paper: #ffffff;
  }
  * { box-sizing: border-box; margin: 0; padding: 0; }
  html, body { width: 1200px; height: 1200px; overflow: hidden; }
  body {
    background: var(--backdrop);
    font-family: "Lato", sans-serif;
    position: relative;
  }
  .card {
    position: absolute;
    left: 250px;
    width: 700px;
    height: 399px;
    border-radius: 34px;
    overflow: hidden;
  }
  .card-front { top: 170px; background: var(--paper); }
  .card-back { top: 631px; background: var(--brand-red); color: var(--paper); }

  /* front */
  .name-band {
    position: absolute;
    left: 0; top: 45px;
    width: 400px; height: 84px;
    background: var(--brand-red);
    color: var(--paper);
    padding: 12px 0 0 35px;
  }
  .person-name { font-weight: 900; font-size: 33px; line-height: 1.1; letter-spacing: 0.2px; }
  .person-title { font-weight: 400; font-size: 19px; line-height: 1.2; margin-top: 1px; }
  .brand-seal {
    position: absolute;
    left: 369px; top: 42px;
    width: 88px; height: 88px;
    border-radius: 50%;
    background: var(--paper);
    border: 6px solid var(--brand-red);
  }
  .brand-name {
    position: absolute;
    left: 472px; top: 54px;
    width: 186px;
    text-align: right;
    color: var(--brand-red);
    font-weight: 900;
    font-size: 22px;
    line-height: 1.12;
    letter-spacing: 0.5px;
  }
  .contact-list, .company-block {
    position: absolute;
    top: 270px;
    list-style: none;
    font-size: 17px;
    line-height: 24.5px;
    color: var(--ink);
  }
  .contact-list { left: 36px; }
  .contact-list li { display: flex; align-items: center; gap: 9px; }
  .contact-list svg { width: 15px; height: 15px; fill: var(--brand-red); flex: none; }
  .company-block { right: 44px; text-align: right; }
  .company-block .company-name { color: var(--brand-red); }

  /* back */
  .mark-ring {
    position: absolute;
    left: 92px; top: 85px;
    width: 230px; height: 230px;
    border-radius: 50%;
    border: 24px solid var(--paper);
    display: flex; align-items: center; justify-content: center;
    text-align: center;
    font-weight: 900; font-size: 20px; line-height: 1.2; letter-spacing: 0.5px;
  }
  .divider {
    position: absolute;
    left: 362px; top: 75px;
    width: 1.5px; height: 248px;
    background: rgba(255,255,255,0.8);
  }
  .services {
    position: absolute;
    left: 401px; top: 72px;
  }
  .services-title { font-weight: 900; font-size: 27px; line-height: 32px; margin-bottom: 1px; }
  .services-list { list-style: none; font-size: 17px; line-height: 24.5px; }
  .services-list li { position: relative; padding-left: 19px; }
  .services-list li::before {
    content: ""; position: absolute; left: 1px; top: 9px;
    width: 6px; height: 6px; border-radius: 50%; background: var(--paper);
  }
</style>
</head>
<body>

<section class="card card-front">
  <div class="name-band">
    <div class="person-name">DANIEL ROURKE</div>
    <div class="person-title">Founder &amp; CEO</div>
  </div>
  <div class="brand-seal"></div>
  <div class="brand-name">TALLOWMERE<br>CONTRACTING LLC</div>

  <ul class="contact-list">
    <li><svg viewBox="0 0 24 24"><path d="M6.6 10.8a15.1 15.1 0 0 0 6.6 6.6l2.2-2.2a1 1 0 0 1 1-.25 11.4 11.4 0 0 0 3.6.57 1 1 0 0 1 1 1V20a1 1 0 0 1-1 1A17 17 0 0 1 3 4a1 1 0 0 1 1-1h3.5a1 1 0 0 1 1 1c0 1.25.2 2.45.57 3.57a1 1 0 0 1-.25 1z"/></svg>(555) 214-7730</li>
    <li><svg viewBox="0 0 24 24"><path d="M7 1h10a2 2 0 0 1 2 2v18a2 2 0 0 1-2 2H7a2 2 0 0 1-2-2V3a2 2 0 0 1 2-2zm0 3v14h10V4zm5 15.5a1.2 1.2 0 1 0 0 2.4 1.2 1.2 0 0 0 0-2.4z"/></svg>(555) 382-1946</li>
    <li><svg viewBox="0 0 24 24"><path d="M6 2h12v5H6zM3 8h18a2 2 0 0 1 2 2v7h-4v5H5v-5H1v-7a2 2 0 0 1 2-2zm4 8v4h10v-4z"/></svg>(555) 603-5518</li>
    <li><svg viewBox="0 0 24 24"><path d="M2 5h20v14H2zm2 2v.5l8 5.5 8-5.5V7z"/></svg>office@tallowmerebuild.com</li>
  </ul>

  <address class="company-block" style="font-style:normal">
    <div class="company-name">Tallowmere Contracting LLC</div>
    <div>Address, City, State</div>
    <div>Country, Zip Code 01235</div>
    <div>www.tallowmerebuild.com</div>
  </address>
</section>

<section class="card card-back">
  <div class="mark-ring">TALLOWMERE<br>CONTRACTING</div>
  <div class="divider"></div>
  <div class="services">
    <h2 class="services-title">OUR SERVICES</h2>
    <ul class="services-list">
      <li>Lorem ipsum</li>
      <li>Aliquam tincidunt</li>
      <li>Vestibulum auctor</li>
      <li>Nunc dignissim</li>
      <li>Cras ornare</li>
      <li>Vivamus vestibulum</li>
      <li>Praesent placerat</li>
      <li>Fusce pellentesque</li>
      <li>Integer vitae</li>
    </ul>
  </div>
</section>

</body>
</html>
```